Christmas / Holiday themed front and back wine label set
Warm Mulled Wine / hot spiced wine
We need a hot spice wine label that screams Christmas / Thanksgiving / the holidays. Need a front and back label set. Label needs to be obvious holiday themed so retailers can display / sell for the Christmas holiday season. Wine is a green, 750ml standard wine bottle, with a dravoke screw top seal. We can pick standard colors for the screw cap to match your label design.
Beverages
Adults 21 to 70 years old. A hot spiced wine, served warm, about the temperature of hot chocolate at holiday parties and family gatherings. It also can be given as a "Christmas gift" to friends, family and holiday workers.
Front label 3 1/2" wide by 4 1/2" tall max size. Back label 3" wide by 4 1/2" tall max size. Some legal text will need to be added after the winning design is selected for the back label. The following text should be incorporated on either the front or back label "Warm Mulled Wine, a light table wine with honey, unfermented cider lemon juices and spices." Also "SERVE WARM but do not boil" Also "Alcohol 9% by volume". On the back label will need to add a UPC number too along with the "GOVERNMENT WARNING"

```html
<!DOCTYPE html>
<html lang="en">
<head>
<meta charset="utf-8">
<title>Holly Cheer – Warm Mulled Wine Label Set</title>
<link href="https://fonts.googleapis.com/css2?family=Great+Vibes&family=Cormorant+Garamond:wght@500;600;700&display=swap" rel="stylesheet">
<style>
  :root {
    --paper: #ffffff;
    --red-top: #c8202a;
    --red-mid: #b5171f;
    --red-deep: #86101a;
    --forest: rgba(110, 10, 18, 0.55);
    --teal: #1e3b44;
    --gold: #eab43c;
    --gold-soft: #f3cf6e;
    --cream: #fbeee0;
  }
  * { margin: 0; padding: 0; box-sizing: border-box; }
  html, body {
    width: 1200px; height: 792px; overflow: hidden;
    background: var(--paper);
  }
  .label-set { position: relative; width: 1200px; height: 792px; }
  .label {
    position: absolute; top: 0; height: 792px;
    overflow: hidden;
    font-family: "Cormorant Garamond", "Times New Roman", serif;
    color: var(--cream);
    text-align: center;
  }
  .label--front { left: 0; width: 612px; }
  .label--back { left: 672px; width: 528px; }

  .label__field {
    position: absolute; left: 0; right: 0; top: 0; height: 570px;
    background: linear-gradient(180deg, var(--red-top) 0%, var(--red-mid) 45%, var(--red-deep) 100%);
  }
  .forest {
    position: absolute; left: 0; right: 0; top: 170px; height: 400px;
    background: linear-gradient(180deg, rgba(120,12,20,0) 0%, var(--forest) 60%, rgba(100,8,16,0.7) 100%);
  }
  .sleigh {
    position: absolute; height: 46px;
    background: linear-gradient(90deg, rgba(90,8,14,0.55), rgba(90,8,14,0.35));
    border-radius: 23px;
  }
  .label--front .sleigh { left: 150px; top: 50px; width: 300px; }
  .label--back .sleigh { left: 140px; top: 50px; width: 300px; }

  .flourish {
    position: absolute; left: 50%; transform: translateX(-50%);
    height: 26px; border-radius: 13px;
    background: radial-gradient(ellipse at center, rgba(234,180,60,0.85) 0%, rgba(234,180,60,0.25) 70%, rgba(234,180,60,0) 100%);
  }
  .flourish--top { top: 40px; width: 200px; }
  .flourish--mid { top: 384px; width: 200px; }

  .gold-rule {
    position: absolute; left: 0; right: 0; top: 570px; height: 16px;
    background: var(--gold);
    border-top: 4px solid var(--gold-soft);
  }
  .gold-rule::after {
    content: ""; position: absolute; left: 0; right: 0; top: 5px; height: 3px;
    background: var(--teal);
  }
  .label__base {
    position: absolute; left: 0; right: 0; top: 586px; bottom: 0;
    background: var(--teal);
  }

  .quality {
    position: absolute; left: 0; right: 0; top: 98px;
    font-size: 19px; font-weight: 700; letter-spacing: 1px;
  }
  .brand {
    position: absolute; left: 0; right: 0; top: 120px;
    font-family: "Great Vibes", cursive;
    font-size: 88px; line-height: 1; color: var(--gold);
  }
  .product {
    position: absolute; left: 0; right: 0; top: 262px;
    font-size: 38px; font-weight: 600; color: var(--gold); letter-spacing: 1px;
  }
  .description {
    position: absolute; left: 110px; right: 110px; top: 326px;
    font-size: 15px; font-weight: 600; line-height: 1.4; text-transform: uppercase;
  }
  .strength {
    position: absolute; left: 0; right: 0; top: 432px;
    font-size: 20px; font-weight: 600; line-height: 1.75;
  }
  .serve-note {
    position: absolute; left: 0; right: 0; top: 660px;
    font-size: 28px; font-weight: 700; color: var(--gold); letter-spacing: 0.5px;
  }
  .serve-note::after {
    content: ""; display: block; width: 44px; height: 3px;
    margin: 8px auto 0; background: var(--gold);
  }

  .audience {
    position: absolute; left: 0; right: 0; top: 98px;
    font-size: 18px; font-weight: 700; line-height: 1.15; text-transform: uppercase;
  }
  .story {
    position: absolute; left: 78px; right: 62px; top: 162px;
    font-size: 17px; font-weight: 600; line-height: 1.55;
    text-transform: uppercase; text-align: justify;
  }
</style>
</head>
<body>
<main class="label-set">

  <section class="label label--front" aria-label="Front label">
    <div class="label__field">
      <div class="forest" role="img" aria-label="Faint silhouette of a pine forest"></div>
      <div class="sleigh" role="img" aria-label="Silhouette of Santa's sleigh pulled by reindeer"></div>
      <div class="flourish flourish--top" role="img" aria-label="Gold ornamental flourish"></div>
      <p class="quality">PREMIUM QUALITY</p>
      <h1 class="brand">Holly Cheer</h1>
      <h2 class="product">WARM MULLED WINE</h2>
      <p class="description">A light table wine with honey, unfermented cider lemon juices and spices</p>
      <div class="flourish flourish--mid" role="img" aria-label="Gold ornamental flourish"></div>
      <p class="strength">ALC. 9%<br>BY VOL . 750ML</p>
    </div>
    <div class="gold-rule"></div>
    <div class="label__base">
    </div>
    <p class="serve-note">SERVE WARM BUT DO NOT BOIL</p>
  </section>

  <section class="label label--back" aria-label="Back label">
    <div class="label__field">
      <div class="forest" role="img" aria-label="Faint silhouette of a pine forest"></div>
      <div class="sleigh" role="img" aria-label="Silhouette of Santa's sleigh pulled by reindeer"></div>
      <p class="audience">Serve to<br>Adults 21 to 70 years old</p>
      <p class="story">A hot spiced wine, served warm, about the temperature of hot chocolate at holiday parties and family gatherings. It also can be given as a "Christmas gift" to friends, family and holiday workers</p>
    </div>
    <div class="gold-rule"></div>
    <div class="label__base"></div>
  </section>

</main>
</body>
</html>
```